VORLEN Website Design

We need a website designed for our company VORLEN. We are a luxury lifestyle club that will provide benefits and services for our members. The site should be clean & sleek, preferably using black and white (or darker colors). (example sites: brimvale.example, tusko.example)

Here is a link of a sample page I did using wix. (https://pelmundry4.sitebuild.example/mypage) This can be used to get a general idea.

Target Market(s)

Upper Middle Class in the United States

Number of Pages Required

5+ page

Font styles to use
Sans Serif
Other font styles liked:
• Arial (or other similar fonts)

Requirements
Must have
• A clean design that is eye-catching and speaks to our company.
Nice to have
• Ideas for copy.

```html
<!DOCTYPE html>
<html lang="en">
<head>
<meta charset="utf-8">
<title>VORLEN — A Members Only Lifestyle Club</title>
<link rel="stylesheet" href="https://fonts.googleapis.com/css2?family=Outfit:wght@400;500;600&family=Roboto:wght@400;500&display=swap">
<style>
:root{
  --ink:#ffffff;
  --muted:#d6d6d6;
  --dim:#9a9a9a;
  --night:#151515;
  --night-2:#1c1c1c;
  --forest:#0f4a26;
  --forest-deep:#0b3a1d;
  --forest-btn:#175a2e;
  --card-line:#4a4a4a;
  --paper:#ffffff;
  --text-dark:#222222;
  --text-grey:#777777;
}
*{box-sizing:border-box;margin:0;padding:0}
html,body{width:1200px;height:3455px;overflow:hidden}
body{position:relative;background:var(--night);color:var(--ink);font-family:"Roboto",Arial,sans-serif}
.abs{position:absolute}
.display{font-family:"Outfit",Arial,sans-serif}

/* header + hero */
.hero{left:0;top:0;width:1200px;height:654px;
  background:radial-gradient(ellipse at 50% 55%,#5e6a3c 0%,#3b4426 40%,#1d2116 80%,#121410 100%)}
.hero-shade{left:0;top:0;width:1200px;height:654px;background:rgba(0,0,0,.28)}
.logo{left:90px;top:30px;font-family:"Outfit",Arial,sans-serif;font-weight:500;font-size:40px;letter-spacing:3px}
.nav{top:40px;left:502px;display:flex;gap:0;font-size:16px;letter-spacing:.3px}
.nav a{color:var(--ink);text-decoration:none;position:absolute;white-space:nowrap}
.nav-apply{left:1021px;top:32px;width:81px;height:36px;border:1px solid var(--ink);font-size:16px;display:flex;align-items:center;justify-content:center}
.nav-rule{left:90px;top:104px;width:1020px;height:1px;background:rgba(255,255,255,.55)}
.hero-title{left:0;top:240px;width:1200px;text-align:center;font-size:54px;font-weight:500}
.hero-sub{left:0;top:318px;width:1200px;text-align:center;font-size:28px;line-height:42px;font-family:"Roboto",Arial,sans-serif}
.btn-learn{left:510px;top:428px;width:178px;height:56px;background:var(--forest-btn);border:1px solid rgba(255,255,255,.6);display:flex;align-items:center;justify-content:center;font-size:24px}
.dots{display:flex;gap:10px}
.dot{width:14px;height:14px;border-radius:50%;border:2px solid var(--ink)}
.dot.on{background:var(--ink)}

/* about */
.about{left:0;top:654px;width:1200px;height:654px;background:linear-gradient(180deg,#1b1b1b,#151515 60%,#1a1a1a)}
.about-bar{left:106px;top:795px;width:72px;height:375px;background:var(--forest)}
.about-photo{left:177px;top:795px;width:420px;height:375px;background:radial-gradient(ellipse at 45% 40%,#f3c57a 0%,#b46a32 35%,#4a2614 75%,#1d0f08 100%)}
.about-title{left:638px;top:806px;font-size:40px;font-weight:500}
.about-text{left:638px;width:450px;font-size:16px;line-height:25.5px;color:var(--ink)}
.btn-outline{border:1px solid var(--ink);display:flex;align-items:center;justify-content:center;font-size:16px}

/* services */
.services{left:0;top:1308px;width:1200px;height:919px;background:radial-gradient(ellipse at 50% 20%,#2c2a24 0%,#1e1d1a 50%,#151515 100%)}
.section-title{left:0;width:1200px;text-align:center;font-size:48px;font-weight:500}
.service-card{width:292px;height:232px;border:1px solid var(--card-line);background:rgba(10,10,10,.55);text-align:center}
.service-card.active{background:var(--forest-deep);border-color:#2f7a48}
.service-card svg{position:absolute;left:116px;top:30px}
.service-card h3{position:absolute;left:0;top:120px;width:100%;font-family:"Roboto",Arial,sans-serif;font-weight:500;font-size:19px}
.service-card p{position:absolute;left:30px;top:158px;width:232px;font-size:14px;line-height:23px;color:var(--muted)}
.pager{display:flex;gap:10px}
.pager span{width:7px;height:7px;border-radius:50%;background:#555}
.pager span.on{background:var(--ink)}

/* experiences */
.experiences{left:0;top:2227px;width:1200px;height:767px;background:radial-gradient(ellipse at 50% 30%,#1b5a32 0%,#12472a 55%,#0d3a21 100%)}
.exp-card{width:511px;height:417px;background:var(--paper);color:var(--text-dark)}
.exp-photo{left:0;top:0;width:511px;height:228px}
.exp-card h3{position:absolute;left:38px;top:262px;font-family:"Roboto",Arial,sans-serif;font-weight:400;font-size:20px}
.exp-card p{position:absolute;left:38px;top:308px;width:440px;font-size:14px;line-height:24px;color:var(--text-grey)}
.read-more{position:absolute;left:38px;top:370px;font-size:13px;font-weight:500;letter-spacing:.3px}
.read-more::after{content:"";position:absolute;left:0;top:24px;width:54px;height:2px;background:var(--text-dark)}

/* footer */
.footer{left:0;top:2994px;width:1200px;height:380px;background:linear-gradient(180deg,#191919,#131313)}
.foot-head{top:3089px;font-size:20px;font-weight:500;letter-spacing:.3px}
.foot-links{top:3140px;display:flex;flex-direction:column;gap:14px;font-size:16px;line-height:20px}
.contact-label{font-size:16px;font-weight:500}
.contact-value{font-size:14px}
.field{left:811px;width:301px;height:37px;background:var(--paper);color:#777;font-size:15px;padding-left:16px;display:flex;align-items:center}
.btn-send{left:811px;top:3275px;width:129px;height:38px;background:var(--forest-btn);display:flex;align-items:center;justify-content:center;font-size:18px;letter-spacing:.5px}
.bottom-bar{left:0;top:3374px;width:1200px;height:81px;background:#0e0e0e}
.copyright{left:0;top:3404px;width:1200px;text-align:center;font-size:13px;color:var(--dim)}
</style>
</head>
<body>

<!-- Hero -->
<div class="abs hero" role="img" aria-label="Photo of an outdoor garden event with decorated chairs and hanging lanterns"></div>
<div class="abs hero-shade"></div>
<div class="abs logo">VORLEN</div>
<nav class="nav">
  <a style="left:502px;top:40px">HOME</a>
  <a style="left:589px;top:40px">ABOUT</a>
  <a style="left:684px;top:40px">SERVICES AND BENEFITS</a>
  <a style="left:914px;top:40px">CONTACT</a>
</nav>
<div class="abs nav-apply">APPLY</div>
<div class="abs nav-rule"></div>
<h1 class="abs hero-title display">A Members Only Lifestyle Club</h1>
<p class="abs hero-sub">VORLEN organizes and supports a ton of private<br>events and parties for our members</p>
<div class="abs btn-learn">Learn More</div>
<div class="abs dots" style="left:565px;top:579px"><span class="dot on"></span><span class="dot"></span><span class="dot"></span></div>

<!-- About -->
<section class="abs about"></section>
<div class="abs about-bar"></div>
<div class="abs about-photo" role="img" aria-label="Photo of a crowd celebrating at a concert under warm stage lights"></div>
<h2 class="abs about-title display">About VORLEN</h2>
<p class="abs about-text" style="top:872px">VORLEN was formed to bring the best services, experiences, and exclusive opportunities to our members. With everything from private member events to private jet travel, the perks of being a VORLEN member are unmatched.</p>
<p class="abs about-text" style="top:986px">Professional athletes, artists, musicians, corporate professionals: Our members come from diverse backgrounds. Comprehensive services like 24/7 concierge, accountants, attorneys, private advisers, planners, investment advisors and more.</p>
<div class="abs btn-outline" style="left:638px;top:1108px;width:92px;height:37px">Apply</div>

<!-- Services -->
<section class="abs services" role="img" aria-label="Dimmed photo of an evening event venue"></section>
<h2 class="abs section-title display" style="top:1436px">Services and Benefits</h2>

<div class="abs service-card" style="left:124px;top:1564px">
  <svg width="60" height="66" viewBox="0 0 60 66" fill="none" stroke="#fff" stroke-width="2"><rect x="4" y="6" width="40" height="54"/><rect x="10" y="12" width="28" height="10"/><path d="M10 30h6M22 30h6M34 30h4M10 40h6M22 40h6M34 40h4M10 50h6M22 50h6M34 50h4"/><path d="M50 8v46l4 6 4-6V8z"/></svg>
  <h3>Accounting Services</h3>
  <p>VORLEN membership provides you with amazing benefits and services</p>
</div>
<div class="abs service-card active" style="left:454px;top:1564px">
  <svg width="60" height="66" viewBox="0 0 60 66" fill="none" stroke="#fff" stroke-width="2"><path d="M4 44l14-14 10 8 22-24"/><path d="M42 12h8v8"/><path d="M8 60V50h6v10M20 60V44h6v16M32 60V40h6v20"/><circle cx="48" cy="50" r="9"/><path d="M48 45v10M45 48h5"/></svg>
  <h3>Investment Services</h3>
  <p>VORLEN membership provides you with amazing benefits and services</p>
</div>
<div class="abs service-card" style="left:785px;top:1564px">
  <svg width="60" height="66" viewBox="0 0 60 66" fill="none" stroke="#fff" stroke-width="2"><path d="M18 10q12-8 24 0v14H18z"/><path d="M20 24q10 16 20 0"/><path d="M8 62V50q0-10 12-12h20q12 2 12 12v12z"/><path d="M26 38l4 10 4-10"/></svg>
  <h3>Lawyer Services</h3>
  <p>VORLEN membership provides you with amazing benefits and services</p>
</div>
<div class="abs service-card" style="left:124px;top:1829px">
  <svg width="60" height="66" viewBox="0 0 60 66" fill="none" stroke="#fff" stroke-width="2"><path d="M2 30L30 6l28 24"/><path d="M8 26v34h44V26"/><rect x="24" y="40" width="12" height="20"/><rect x="13" y="34" width="7" height="7"/><rect x="40" y="34" width="7" height="7"/><path d="M42 12v8h6v-3"/></svg>
  <h3>Real Estate Services</h3>
  <p>VORLEN membership provides you with amazing benefits and services</p>
</div>
<div class="abs service-card" style="left:454px;top:1829px">
  <svg width="60" height="66" viewBox="0 0 60 66" fill="none" stroke="#fff" stroke-width="2"><path d="M10 20q-6 6 0 16l14 18q8 8 16 2l4-4-8-8-5 4-12-14 4-5-8-8z"/><circle cx="44" cy="18" r="13"/><text x="44" y="22" fill="#fff" stroke="none" font-size="10" text-anchor="middle" font-family="Arial,sans-serif">24/7</text></svg>
  <h3>24/7 Concierge</h3>
  <p>VORLEN membership provides you with amazing benefits and services</p>
</div>
<div class="abs service-card" style="left:785px;top:1829px">
  <svg width="60" height="66" viewBox="0 0 60 66" fill="none" stroke="#fff" stroke-width="2"><path d="M4 34l8-2 4-22 6 2-2 18h26q8 2 10 6-2 4-10 6H22l-6 18-6-2 2-16-8-2z"/><path d="M30 30l-6-16h6l10 16"/></svg>
  <h3>Private Jet Travel</h3>
  <p>VORLEN membership provides you with amazing benefits and services</p>
</div>
<div class="abs pager" style="left:589px;top:2123px"><span></span><span class="on"></span></div>

<!-- Experiences -->
<section class="abs experiences"></section>
<h2 class="abs section-title display" style="top:2340px">Experiences</h2>
<article class="abs exp-card" style="left:62px;top:2460px">
  <div class="abs exp-photo" role="img" aria-label="Photo of travellers boarding a private jet on a red carpet" style="background:linear-gradient(180deg,#8fa6bf 0%,#c9d2da 45%,#7b7d80 70%,#5a5c5f 100%)"></div>
  <h3>Neque porro quisquam est dolorem</h3>
  <p>Praesent elementum elit at tellus nec ultricies sit amet porttitor mattis enim In massa libero interdum nec interdum vel blandi</p>
  <span class="read-more">READ MORE</span>
</article>
<article class="abs exp-card" style="left:594px;top:2460px">
  <div class="abs exp-photo" role="img" aria-label="Photo of stacked coins in front of a city skyline" style="background:linear-gradient(135deg,#1d3557 0%,#3e6a99 45%,#8fb4d6 75%,#4a5d74 100%)"></div>
  <h3>Dolorem ipsum quia dolor sit amet</h3>
  <p>Praesent elementum elit at tellus nec ultricies sit amet porttitor mattis enim In massa libero interdum nec interdum</p>
  <span class="read-more">READ MORE</span>
</article>

<!-- Footer -->
<footer class="abs footer"></footer>
<h4 class="abs foot-head" style="left:94px">CONTACT US</h4>
<svg class="abs" style="left:94px;top:3143px" width="20" height="16" viewBox="0 0 20 16" fill="none" stroke="#fff" stroke-width="1.5"><rect x="1" y="1" width="18" height="14"/><path d="M1 1l9 8 9-8"/></svg>
<div class="abs" style="left:122px;top:3140px"><div class="contact-label">EMAIL ADDRESS</div><div class="contact-value">info@vorlenclub.example</div></div>
<svg class="abs" style="left:94px;top:3212px" width="20" height="20" viewBox="0 0 20 20" fill="none" stroke="#fff" stroke-width="1.5"><path d="M4 2l4 4-2 3q2 4 5 5l3-2 4 4-3 3Q8 18 2 5z"/></svg>
<div class="abs" style="left:122px;top:3208px"><div class="contact-label">PHONE NUMBER</div><div class="contact-value">0400 555 018</div></div>

<h4 class="abs foot-head" style="left:387px">LINKS</h4>
<div class="abs foot-links" style="left:387px"><span>Home</span><span>About Us</span><span>Support Center</span><span>Services</span></div>

<h4 class="abs foot-head" style="left:594px">RESOURCES</h4>
<div class="abs foot-links" style="left:594px"><span>Benefits</span><span>Features</span><span>Blog</span><span>Contact Us</span></div>

<h4 class="abs foot-head" style="left:808px">GET IN TOUCH</h4>
<div class="abs field" style="top:3132px">Your Name</div>
<div class="abs field" style="top:3182px">Email address</div>
<div class="abs field" style="top:3225px">Phone</div>
<div class="abs btn-send">SEND</div>

<div class="abs bottom-bar"></div>
<p class="abs copyright">© 2018 Company Name&nbsp; All right reserved</p>

</body>
</html>
```